packaging Design Project

We would like to receive amazing design for our packaging sanitary napkin brand TORVELLE to catch customers
1)we have attached a file named CALDORA design but it is just a reference for taking the information please avoid to do a similar design as the brands are differents .As reference for the map of the design some modifications should be done on the sizes as per the following:
instead 12mm/24mm/90mm/24mm/12mm
it should be 25mm/35mm/120mm/35mm/25mm
instead 83mm/48mm/83mm/48mm/
it should be 105mm/65mm/105mm/65mm
2)our contact information have been changed and the new ones are as per the following:
Phone:(509)3-482-6051
:(509)3-396-1438
E-mail:info@harbeckwholesale.example
3)we have attached the TORVELLE sanitary pictures to be redesigned as per Brindle is done on its packaging.This is a very important point of the the design you will submit.
4)our company logo is attached
5)we need the design in CMYK format as it is for printing with the specified pantone number .
6)you can pick pictures from framequarry.example if you win we will buy it.
7)Please go to the supermarket or drugstore to have a better idea how the design should be but we are not required a copy of any brand.
8)five water drops in red or pink color should be in the both front to indicate the high absorption quality.
9) 8 pads.serviettes.toallas to indicate the qty per package.
10)a big word (MAXI) should be writted in the both front to indicate its high absorption.
11)275mm to indicate the lenght.
12)write SANITARY NAPKIN below the word TORVELLE.
13)reduce the size of our company logo and put it in the both front at the top on the left side.
14)please read the brief time to time because we are upgraded information time to time too.
15)Any doubt or question please send me a message.
N.B: the packaging design should be able to compete with BRINDLE PLUSH or Velumi so be creative to develop an amazing and innovative design.
Updates
please redesign the torvelle sanitary picture with each detail to be attractive,this is one of most importamt part of the design.
Reason: need more designs and some designers have required more time.
now the deadline is for may 13th.
please do not put barcode number.
Reason: need of amazing designs
don't work with the caldora sanitary picture but with the torvelle sanitary picture.you should design the torvelle sanitary picture to refelct all of its details to be amazing.
Reason: lack of good designs
Target Market(s)
woman from 12 to 45 years old
Industry/Entity Type
It Company
Requirements
Must have
- A)the design should have two fronts and the same information in the both front.
B) (MAXI) should be writted in the both front to indicate its high capacity of absorption.
C)five blood drops in red or pink color should be in the both front to indicate the high absorption quality.
D) 8 pads.serviettes.toallas to indicate the qty per package.
E)275mm to indicate the lenght
F)write SANITARY NAPKIN below the word
G)use fresh and innovative colors but feminine colors .
Nice to have
-reduce the size of our company logo and put it in the both front at the top of the left side.
Should not have
- -please don't put flowers because the pad dosen't have any scent or perfume.
-Please do not put barcode number.

```html
<!DOCTYPE html>
<html lang="en">
<head>
<meta charset="utf-8">
<title>TORVELLE Maxi – packaging dieline</title>
<link rel="stylesheet" href="https://fonts.googleapis.com/css2?family=Barlow+Semi+Condensed:wght@300;400&display=swap">
<style>
  :root {
    --paper: #ffffff;
    --dieline: #dcdcdc;
    --fold: #8a9aab;
    --band-pink: #f298c4;
    --brand-pink: #ec7cb6;
    --text-white: #ffffff;
    --sky-deep: #4e5d6a;
    --sky-mid: #7c8a8c;
    --cloud-cream: #d9d3a8;
    --logo-navy: #3e5366;
  }
  html, body {
    margin: 0;
    width: 1200px;
    height: 1000px;
    overflow: hidden;
    background: var(--paper);
  }
  .canvas { display: block; width: 1200px; height: 1000px; }
  .type { font-family: "Barlow Semi Condensed", "Arial Narrow", sans-serif; }
  .brand-name { fill: var(--text-white); font-weight: 400; }
  .product-line { fill: var(--text-white); font-weight: 300; }
  .absorbency { fill: var(--brand-pink); font-weight: 300; }
  .pack-count { fill: var(--text-white); font-weight: 400; }
  .logo-name { fill: var(--text-white); font-weight: 400; }
  .band { fill: var(--band-pink); }
  .flap { fill: var(--paper); stroke: var(--dieline); stroke-width: 1; }
  .fold-line { stroke: var(--fold); stroke-width: 1; opacity: .55; }
  .cut-line { stroke: var(--dieline); stroke-width: 1; fill: none; }
  .drop { fill: var(--brand-pink); }
  .icon-disc { fill: var(--brand-pink); }
  .icon-pad { fill: var(--text-white); }
  .logo-disc { fill: var(--logo-navy); }
</style>
</head>
<body>
<svg class="canvas type" viewBox="0 0 1200 1000" xmlns="http://www.w3.org/2000/svg">
  <defs>
    <linearGradient id="sky-front" x1="0" y1="0" x2="0" y2="1">
      <stop offset="0" stop-color="#56646f"/>
      <stop offset=".35" stop-color="#a9a78e"/>
      <stop offset=".5" stop-color="#d9d3a8"/>
      <stop offset=".7" stop-color="#7f8b8a"/>
      <stop offset="1" stop-color="#4a5966"/>
    </linearGradient>
    <linearGradient id="sky-side" x1="1" y1="0" x2="0" y2="0">
      <stop offset="0" stop-color="#4a5966"/>
      <stop offset=".3" stop-color="#8f9786"/>
      <stop offset=".55" stop-color="#d4cea4"/>
      <stop offset=".75" stop-color="#7d8a89"/>
      <stop offset="1" stop-color="#5a6872"/>
    </linearGradient>

    <g id="front-panel-content">
      <circle class="logo-disc" cx="221" cy="257" r="14"/>
      <text class="logo-name" x="221" y="259" font-size="5" text-anchor="middle">HARBECK</text>
      <text class="brand-name" x="203" y="337" font-size="80" textLength="230" lengthAdjust="spacingAndGlyphs">TORVELLE</text>
      <text class="product-line" x="258" y="356" font-size="15" textLength="111" lengthAdjust="spacingAndGlyphs">SANITARY NAPKIN</text>
      <text class="absorbency" x="205" y="450" font-size="120" textLength="228" lengthAdjust="spacingAndGlyphs">MAXI</text>
      <g class="drops">
        <path class="drop" d="M208 465 q-3 5 -3 7 a3 3 0 0 0 6 0 q0 -2 -3 -7z"/>
        <path class="drop" d="M216 465 q-3 5 -3 7 a3 3 0 0 0 6 0 q0 -2 -3 -7z"/>
        <path class="drop" d="M224 465 q-3 5 -3 7 a3 3 0 0 0 6 0 q0 -2 -3 -7z"/>
        <path class="drop" d="M232 465 q-3 5 -3 7 a3 3 0 0 0 6 0 q0 -2 -3 -7z"/>
        <path class="drop" d="M240 465 q-3 5 -3 7 a3 3 0 0 0 6 0 q0 -2 -3 -7z"/>
      </g>
      <text class="pack-count" x="250" y="474" font-size="8" textLength="116" lengthAdjust="spacingAndGlyphs">8 PADS • SERVIETTES • TOALLAS</text>
      <circle class="icon-disc" cx="384" cy="469" r="16"/>
      <rect class="icon-pad" x="374" y="464" width="20" height="10" rx="5" transform="rotate(-30 384 469)"/>
    </g>
  </defs>

  <!-- Left dieline: two fronts and pink gussets -->
  <g class="dieline-left">
    <rect class="flap" x="11" y="62" width="611" height="865"/>
    <line class="cut-line" x1="11" y1="228" x2="622" y2="228"/>
    <line class="cut-line" x1="11" y1="494" x2="622" y2="494"/>
    <line class="cut-line" x1="11" y1="660" x2="622" y2="660"/>

    <rect class="band" x="75" y="62" width="483" height="166"/>
    <rect class="band" x="75" y="494" width="483" height="166"/>

    <g role="img" aria-label="Photograph of a cloudy sky over the sea">
      <rect x="75" y="228" width="483" height="266" fill="url(#sky-front)"/>
    </g>
    <g role="img" aria-label="Photograph of a cloudy sky over the sea">
      <rect x="75" y="660" width="483" height="267" fill="url(#sky-front)" transform="rotate(180 316.5 793.5)"/>
    </g>

    <line class="fold-line" x1="163" y1="62" x2="163" y2="927"/>
    <line class="fold-line" x1="470" y1="62" x2="470" y2="927"/>

    <g class="front front-top"><use href="#front-panel-content"/></g>
    <g class="front front-bottom" transform="rotate(180 316.5 793.5) translate(0 432)"><use href="#front-panel-content"/></g>
  </g>

  <!-- Right dieline: side panel -->
  <g class="dieline-right">
    <g role="img" aria-label="Photograph of a cloudy sky over the sea, vertical">
      <rect x="650" y="62" width="475" height="850" fill="url(#sky-side)"/>
    </g>
    <line class="fold-line" x1="650" y1="216" x2="1125" y2="216"/>
    <line class="fold-line" x1="650" y1="757" x2="1125" y2="757"/>

    <circle class="logo-disc" cx="1068" cy="320" r="25"/>
    <text class="logo-name" x="1068" y="323" font-size="8" text-anchor="middle" transform="rotate(90 1068 320)">HARBECK</text>

    <g transform="translate(930 290) rotate(90)">
      <text class="brand-name" x="0" y="0" font-size="140" textLength="405" lengthAdjust="spacingAndGlyphs">TORVELLE</text>
    </g>
    <g transform="translate(897 290) rotate(90)">
      <text class="product-line" x="0" y="0" font-size="30" textLength="265" lengthAdjust="spacingAndGlyphs">SANITARY NAPKIN</text>
    </g>
    <g transform="translate(722 290) rotate(90)">
      <text class="absorbency" x="0" y="0" font-size="235" textLength="405" lengthAdjust="spacingAndGlyphs">MAXI</text>
    </g>

    <circle class="icon-disc" cx="686" cy="604" r="22"/>
    <rect class="icon-pad" x="672" y="597" width="28" height="14" rx="7" transform="rotate(60 686 604)"/>
  </g>
</svg>
</body>
</html>
```